VQB 2023 Postcard

We need a postcard created for an upcoming trade show. We had something made for our sister company a while back and are interested in a similar look. We have included images and some layouts that can be used along with our logo. We like earthy colors, gray and black are okay too. We would like it to be 5x7 and landscape orientation. We have attached the wording we would like to see on the back of the card with changes made in red.
Target Market(s)
retailers
Industry/Entity Type
wedding ring
Colors
Designer to choose only greyscale colors for use in the design.

```html
<!DOCTYPE html>
<html lang="en">
<head>
<meta charset="utf-8">
<title>VQB 2023 Postcard</title>
<link rel="stylesheet" href="https://fonts.googleapis.com/css2?family=Cinzel:wght@400;600&family=Lato:wght@400;700&display=swap">
<style>
  :root {
    --page: #e4e4e4;
    --ink-dark: #141414;
    --charcoal: #1e1e1e;
    --panel: #2b2b2b;
    --mid-gray: #8a8a8a;
    --light-gray: #d6d6d6;
    --paper: #f4f4f2;
    --white: #ffffff;
    --accent: #c0392b;
    --rule: #4a4a4a;
  }
  * { box-sizing: border-box; margin: 0; padding: 0; }
  html, body { width: 720px; height: 1200px; overflow: hidden; }
  body {
    background: var(--page);
    font-family: "Lato", sans-serif;
    position: relative;
  }
  .postcard {
    position: absolute;
    left: 40px;
    width: 640px;
    height: 457px;
    overflow: hidden;
    box-shadow: 0 6px 18px rgba(0,0,0,0.25);
  }
  .postcard--front { top: 110px; background: var(--white); }
  .postcard--back {
    top: 632px;
    background: linear-gradient(160deg, #2c2c2c 0%, #151515 55%, #0c0c0c 100%);
    color: var(--white);
  }

  /* Front */
  .brand-panel {
    position: absolute; left: 0; top: 0; width: 150px; height: 260px;
    background: linear-gradient(180deg, #2a2a2a, #151515);
    display: flex; flex-direction: column; align-items: center; padding-top: 34px;
  }
  .brand-mark {
    width: 62px; height: 62px; border: 2px solid var(--light-gray);
  }
  .brand-name {
    margin-top: 14px; color: var(--light-gray);
    font-family: "Lato", sans-serif; font-weight: 400;
    font-size: 15px; letter-spacing: 3px; text-align: center; line-height: 1.35;
  }
  .photo { position: absolute; }
  .photo--band-top { left: 152px; top: 0; width: 488px; height: 86px;
    background: linear-gradient(90deg, #f2f2f2, #cfcfcf 45%, #efefef); }
  .photo--rose { left: 152px; top: 88px; width: 80px; height: 85px;
    background: radial-gradient(circle at 50% 55%, #d9a48e 0%, #f3ece8 60%); }
  .photo--gold { left: 234px; top: 88px; width: 80px; height: 85px;
    background: radial-gradient(circle at 50% 55%, #d8b25e 0%, #f4efe3 60%); }
  .photo--pair { left: 316px; top: 88px; width: 80px; height: 85px;
    background: radial-gradient(circle at 50% 55%, #bdbdbd 0%, #f3f3f3 60%); }
  .photo--dark { left: 398px; top: 88px; width: 242px; height: 85px;
    background: linear-gradient(120deg, #1a1a1a, #4b4b4b 50%, #1f1f1f); }
  .photo--silver-row { left: 152px; top: 175px; width: 316px; height: 85px;
    background: linear-gradient(90deg, #f5f5f5, #d2d2d2 30%, #f2f2f2 55%, #cacaca 80%, #f1f1f1); }
  .photo--gold-dark { left: 470px; top: 175px; width: 170px; height: 85px;
    background: linear-gradient(120deg, #222, #6d5a3a 55%, #2a2a2a); }
  .photo--table { left: 0; top: 262px; width: 640px; height: 195px;
    background: linear-gradient(180deg, #eae8e4 0%, #d9d5ce 55%, #b9b2a6 100%); }

  /* Back */
  .back-title {
    position: absolute; top: 26px; left: 0; width: 100%; text-align: center;
    font-family: "Cinzel", serif; font-weight: 600; font-size: 24px; letter-spacing: 2px;
  }
  .back-subtitle {
    position: absolute; top: 62px; left: 0; width: 100%; text-align: center;
    font-size: 11px; color: var(--light-gray); letter-spacing: 0.5px;
  }
  .offer-list {
    position: absolute; left: 34px; top: 104px; width: 300px; list-style: none;
  }
  .offer-list li {
    display: flex; gap: 12px; align-items: flex-start;
    font-size: 13px; line-height: 1.35; margin-bottom: 19px; color: var(--white);
  }
  .offer-list svg { flex: none; margin-top: 2px; }
  .divider {
    position: absolute; left: 350px; top: 104px; width: 1px; height: 240px; background: var(--rule);
  }
  .feature-list {
    position: absolute; left: 372px; top: 100px; width: 236px; list-style: none;
  }
  .feature-list li {
    font-size: 11px; letter-spacing: 0.8px; padding: 7px 0 7px 14px;
    border-bottom: 1px solid var(--rule); position: relative; color: var(--light-gray);
  }
  .feature-list li::before {
    content: ""; position: absolute; left: 2px; top: 12px;
    width: 5px; height: 5px; background: var(--mid-gray);
  }
  .contact-bar {
    position: absolute; left: 0; bottom: 0; width: 100%; height: 82px;
    border-top: 1px solid var(--rule);
    display: flex; justify-content: space-between; align-items: center;
    padding: 0 34px;
  }
  .tagline { font-size: 11px; letter-spacing: 1.5px; color: var(--light-gray); }
  .phone-line { margin-top: 4px; }
  .phone { font-size: 22px; font-weight: 700; color: var(--accent); letter-spacing: 1px; }
  .phone-note { font-size: 11px; color: var(--mid-gray); margin-left: 6px; }
  .address { font-size: 8px; line-height: 1.6; color: var(--mid-gray); text-align: right; }
</style>
</head>
<body>

<section class="postcard postcard--front">
  <div class="brand-panel">
    <div class="brand-mark"></div>
    <div class="brand-name">HALCYON<br>BANDS</div>
  </div>
  <div class="photo photo--band-top" role="img" aria-label="Row of silver and two-tone wedding bands on white"></div>
  <div class="photo photo--rose" role="img" aria-label="Rose gold wedding bands"></div>
  <div class="photo photo--gold" role="img" aria-label="Yellow gold wedding bands"></div>
  <div class="photo photo--pair" role="img" aria-label="Pair of white gold bands"></div>
  <div class="photo photo--dark" role="img" aria-label="Silver rings on a dark background"></div>
  <div class="photo photo--silver-row" role="img" aria-label="Assorted platinum bands on white"></div>
  <div class="photo photo--gold-dark" role="img" aria-label="Gold band on dark stone"></div>
  <div class="photo photo--table" role="img" aria-label="Wedding bands resting on a pale table with soft background"></div>
</section>

<section class="postcard postcard--back">
  <h1 class="back-title">PREMIUM CUSTOMIZED PROGRAMS</h1>
  <p class="back-subtitle">Promote your own brand, rings stamped with your specified logo.</p>

  <ul class="offer-list">
    <li><svg width="14" height="14" viewBox="0 0 14 14"><path d="M2 7l3.5 3.5L12 3" fill="none" stroke="#d6d6d6" stroke-width="2"/></svg><span>Offer rings in any width, 3 thicknesses and all PRECIOUS METALS</span></li>
    <li><svg width="14" height="14" viewBox="0 0 14 14"><path d="M2 7l3.5 3.5L12 3" fill="none" stroke="#d6d6d6" stroke-width="2"/></svg><span>Combine &amp; customize 3300 ring designs</span></li>
    <li><svg width="14" height="14" viewBox="0 0 14 14"><path d="M2 7l3.5 3.5L12 3" fill="none" stroke="#d6d6d6" stroke-width="2"/></svg><span>Sell in Platinum, 18kt, 14kt &amp; 10kt</span></li>
    <li><svg width="14" height="14" viewBox="0 0 14 14"><path d="M2 7l3.5 3.5L12 3" fill="none" stroke="#d6d6d6" stroke-width="2"/></svg><span>Samples kits starting as low as $300 PROGRAM</span></li>
    <li><svg width="14" height="14" viewBox="0 0 14 14"><path d="M2 7l3.5 3.5L12 3" fill="none" stroke="#d6d6d6" stroke-width="2"/></svg><span>Performance MONEY BACK Guarantee</span></li>
  </ul>

  <div class="divider"></div>

  <ul class="feature-list">
    <li>EASY PRICING SYSTEM</li>
    <li>FREE SHIPPING</li>
    <li>SCRAP BUYOUT OPTIONS</li>
    <li>PRE-TAGGED SAMPLES</li>
    <li>1 WEEK TURNAROUND</li>
    <li>COMPETITIVE PRICING</li>
    <li>FAMILY OWNED AND OPERATED</li>
    <li>MADE PROUDLY IN THE USA</li>
  </ul>

  <div class="contact-bar">
    <div>
      <div class="tagline">YOUR TRUSTED SOURCE FOR RINGS</div>
      <div class="phone-line"><span class="phone">800-555-0147</span><span class="phone-note">for information</span></div>
    </div>
    <div class="address">
      210 Harbor Avenue, Suite 12, Riverton NY 10001<br>
      Ph: 800-555-0147 | F: 800-555-0148 | info@halcyonbands.com<br>
      www.halcyonbands.com
    </div>
  </div>
</section>

</body>
</html>
```